indépendant en tant que Massothérapeute et Préparateur Mental, j'ai besoin de ...

Massothérapeute et préparateur mental indépendant, je recherche une carte de visite sobre et dynamique, sans images liées au massage ou à la préparation mentale mais intégrant mon logo. Les couleurs que j'aime bien sont : Blanc, gris, anthracite, noir et jaune

Contact Information for Business Card

carte de préférence Horizontale
neutre qui puisse toucher le deux domaines Massothérapie et préparation mentale

Requirements
Must have
• mon projet doit intégrer au recto:
LOGO
Loïc Vermande
078 315 26 49
info@loicvermande-exemple.ch
et éventuellement www.loicvermande-exemple.ch

et au verso les deux adresses:

Chemin des Ormelets 27B
1400 Yverdon-les-Bains

Rue des Tanneries 9
1700 Fribourg

Should not have
• mon projet ne doit pas contenir d'image en liens avec le massage ni la préparation mentale.

```html
<!DOCTYPE html>
<html lang="fr">
<head>
<meta charset="utf-8">
<title>Loïc Vermande – Cartes de visite</title>
<link rel="stylesheet" href="https://fonts.googleapis.com/css2?family=Lato:wght@400;700&display=swap">
<style>
  :root {
    --backdrop: #e4e4e6;
    --card: #e9e9ec;
    --yellow: #e8e36a;
    --pin: #ddd762;
    --ink: #111111;
  }
  * { box-sizing: border-box; margin: 0; padding: 0; }
  html, body {
    width: 1200px; height: 801px; overflow: hidden;
    background: var(--backdrop);
    font-family: "Lato", sans-serif;
    color: var(--ink);
  }
  .canvas { position: relative; width: 1200px; height: 801px; }

  .card {
    position: absolute;
    left: 355px; width: 514px; height: 308px;
    background: var(--card);
  }
  .card--back { top: 46px; }
  .card--front { top: 423px; }

  /* Back: addresses */
  .address-panel {
    position: absolute; left: 21px; top: 22px; right: 21px; bottom: 21px;
    background: var(--yellow);
  }
  .pin-mark { position: absolute; left: 170px; top: 41px; width: 130px; height: 190px; }
  .back-name {
    position: absolute; right: 287px; top: 135px;
    font-weight: 700; font-size: 13px; letter-spacing: 0.2px;
  }
  .addresses {
    position: absolute; left: 210px; top: 90px;
    font-size: 13.5px; line-height: 18px; letter-spacing: 0.3px;
  }
  .address-divider {
    width: 28px; height: 1px; background: var(--ink);
    margin: 8px 0 9px;
  }

  /* Front: contact */
  .holder-name {
    position: absolute; left: 33px; top: 42px;
    font-size: 21px; font-weight: 700; letter-spacing: 0.5px;
  }
  .contact-list {
    position: absolute; left: 34px; top: 206px;
    list-style: none; font-size: 13px; letter-spacing: 0.4px; line-height: 21.5px;
  }
  .contact-list b { font-weight: 700; margin-right: 4px; }
  .signature {
    position: absolute; right: 36px; top: 226px;
    text-align: right;
  }
  .signature-name {
    display: flex; align-items: center; justify-content: flex-end; gap: 7px;
    font-size: 17px; font-weight: 700; letter-spacing: 0.3px;
  }
  .signature-name::before {
    content: ""; width: 11px; height: 11px; background: var(--ink);
  }
  .signature-role {
    margin-top: 3px;
    font-size: 7.5px; font-weight: 700; letter-spacing: 0.3px;
  }
</style>
</head>
<body>
<main class="canvas">
  <section class="card card--back">
    <div class="address-panel">
      <svg class="pin-mark" viewBox="0 0 130 190" aria-hidden="true">
        <path d="M65 0C29 0 0 29 0 65c0 48 52 98 58 120a7 7 0 0 0 14 0C78 163 130 113 130 65 130 29 101 0 65 0z" fill="var(--pin)"/>
      </svg>
      <div class="back-name">Loïc Vermande</div>
      <div class="addresses">
        <p>Chemin des Ormelets 27B<br>1400 Yverdon-les-Bains</p>
        <div class="address-divider"></div>
        <p>Rue des Tanneries 9<br>1700 Fribourg</p>
      </div>
    </div>
  </section>

  <section class="card card--front">
    <h1 class="holder-name">Loïc Vermande</h1>
    <ul class="contact-list">
      <li><b>M</b>: 078 315 26 49</li>
      <li><b>E</b>&nbsp;: info@loicvermande-exemple.ch</li>
      <li><b>W</b>: www.loicvermande-exemple.ch</li>
    </ul>
    <div class="signature">
      <div class="signature-name">Loïc Vermande</div>
      <div class="signature-role">MASSOTHÉRAPEUTE / PRÉPARATEUR MENTAL</div>
    </div>
  </section>
</main>
</body>
</html>
```